Nutritional Supplement Products Label

We need a label design for a nutritional supplement product line. The product line name is Lumorra and the tagline is "the cleanest nutritional supplement on the planet". Therefore the label needs to be clean, professional and not overly done. It also needs to communicate a revived life and renewed health if possible. I have attached a word document with more details.
Target Market(s)
Primarily women ages 30-50. Professional women and stay at home mothers. The healthy minded mothers (and men).
Industry/Entity Type
Health
Look and feel

```html
<!DOCTYPE html>
<html lang="en">
<head>
<meta charset="UTF-8">
<title>Lumorra Multi - Restore Label</title>
<link rel="stylesheet" href="https://fonts.googleapis.com/css2?family=Arimo:ital,wght@0,400;0,700;1,400;1,700&display=swap">
<style>
  :root {
    --paper: #ffffff;
    --ink-green: #3f9a3a;
    --ink-blue: #2f9ec8;
    --ink-grey: #4a4f55;
    --band-blue: #1f95cf;
    --band-light: #5bb8e4;
    --water-deep: #2f6fb0;
    --water-mid: #8fc0e2;
    --water-pale: #dcedf8;
    --petal: #9fd0e4;
    --petal-deep: #5aa6c8;
  }
  * { margin: 0; padding: 0; box-sizing: border-box; }
  html, body {
    width: 835px;
    height: 1200px;
    overflow: hidden;
    background: var(--paper);
  }
  .label {
    position: relative;
    width: 835px;
    height: 1200px;
    overflow: hidden;
    background: linear-gradient(180deg, var(--paper) 0%, var(--paper) 62%, #cfe6f5 78%, #e9f4fb 90%, var(--paper) 100%);
    font-family: "Arimo", Arial, sans-serif;
  }
  .brand {
    position: absolute;
    left: 22px;
    top: 118px;
    display: flex;
    align-items: center;
    gap: 12px;
    font-size: 46px;
    font-weight: 700;
    color: var(--ink-green);
  }
  .brand-dot {
    width: 16px;
    height: 16px;
    border-radius: 50%;
    background: var(--ink-green);
  }
  .splash-art {
    position: absolute;
    left: 560px;
    top: 40px;
    width: 275px;
    height: 140px;
    background: radial-gradient(ellipse at 80% 45%, var(--water-deep) 0%, var(--water-mid) 35%, rgba(220,237,248,0.6) 65%, rgba(255,255,255,0) 85%);
  }
  .flower-art {
    position: absolute;
    left: 262px;
    top: 118px;
    width: 330px;
    height: 340px;
    background: radial-gradient(ellipse at 50% 50%, var(--petal-deep) 0%, var(--petal) 38%, #d4ebf4 62%, rgba(255,255,255,0) 78%);
  }
  .product-name {
    position: absolute;
    left: 0;
    right: 0;
    top: 470px;
    text-align: center;
    font-size: 72px;
    font-weight: 700;
    letter-spacing: 1px;
    line-height: 1;
  }
  .product-name .word-lead { color: var(--ink-green); }
  .product-name .word-tail { color: var(--ink-blue); }
  .product-type {
    position: absolute;
    left: 0;
    right: 0;
    top: 565px;
    text-align: center;
    font-size: 40px;
    line-height: 1;
    color: var(--ink-blue);
  }
  .wave-art {
    position: absolute;
    left: 0;
    top: 640px;
    width: 835px;
    height: 330px;
    background: linear-gradient(180deg, var(--water-deep) 0%, #5f9bd0 30%, var(--water-mid) 55%, var(--water-pale) 80%, rgba(220,237,248,0) 100%);
    clip-path: path("M0 0 C90 30 200 70 330 80 C450 88 560 60 690 50 C760 44 810 30 835 20 L835 330 L0 330 Z");
  }
  .count {
    position: absolute;
    left: 0;
    right: 0;
    top: 1012px;
    text-align: center;
    font-size: 32px;
    color: var(--ink-grey);
  }
  .tag-band {
    position: absolute;
    left: 0;
    top: 1080px;
    width: 835px;
    height: 58px;
    background: linear-gradient(90deg, var(--band-blue) 0%, var(--band-light) 50%, var(--band-blue) 100%);
    display: flex;
    align-items: center;
    justify-content: center;
  }
  .tagline {
    font-style: italic;
    font-size: 30px;
    color: #ffffff;
  }
</style>
</head>
<body>
  <div class="label">
    <div class="brand"><span class="brand-dot"></span>Lumorra</div>
    <div class="splash-art" role="img" aria-label="Splash of clear blue water"></div>
    <div class="flower-art" role="img" aria-label="Five-petal flower formed from blue water"></div>
    <h1 class="product-name"><span class="word-lead">MULTI</span> <span class="word-tail">- RESTORE</span></h1>
    <p class="product-type">Men's Multivitamin</p>
    <div class="wave-art" role="img" aria-label="Rolling wave of blue water"></div>
    <p class="count">90 Vegetarian Capsules</p>
    <div class="tag-band"><p class="tagline">the cleanest supplement on the planet</p></div>
  </div>
</body>
</html>
```